Anatomic 3D models + Urological Robotic surgery site

I want a website to represent my business as a developer of 3D models (reconstructions based on CT and MRI scans) and urological robotic surgery. The main point I need on my website is that it is modern, very attractive, clean, responsive and an interaction that differentiate me from the usual websites they have in my market. The site will be in portuguese and I'll provide the content to be used. The company name would be my name: Dr Renato Vilhena. The colors and other choices I made here are not final decisions. If you have a suggestion you, they are welcome.

Target Market(s)

My patients

Industry/Entity Type

Medical

Coding

Number of Pages Required

1 page

Font styles to use
Sans Serif

Colors
0054AA
0677BA
7BADD7
CADEEF
E8F1F8
0094D4
00A9DD
6FCCEA
C7EBF8
E9F6FB
00AB8E
00BBA5
67D7C9
C6EFE9
E9F9F6
59FF00
82FF00
B8FF75
E3FFCB
F4FFEA
FFC000
F8CF3A
FAE287
FDF2CF
FEFAEE
F0912C
F2A743
F7CA91
FBE8D2
FDF5EE
A7469A
B969AE
D3A5CF
EDDBEB
F8F0F9
6B429C
8869AF
B7A5CE
E3DAEB
F3F0F8

Requirements
Must have
• Responsive, clean, modern, attractive, stand out from usual sites.
Should not have
• Antiquate boring designs.

```html
<!DOCTYPE html>
<html lang="pt-BR">
<head>
<meta charset="UTF-8">
<title>Dr. Renato Vilhena — Urologia e Cirurgia Minimamente Invasiva</title>
<link href="https://fonts.googleapis.com/css2?family=Lato:wght@400;700;900&display=swap" rel="stylesheet">
<style>
:root{
  --blue:#1f4f9f;
  --blue-dark:#1b4793;
  --sky:#1f9ad6;
  --sky-soft:#8fcbea;
  --tint:#e1f1fa;
  --ink:#111;
  --text:#4a4a4a;
  --white:#fff;
}
*{box-sizing:border-box;margin:0;padding:0}
html,body{width:1200px;height:4099px;overflow:hidden}
body{font-family:'Lato',sans-serif;color:var(--text);background:var(--white);font-size:14.5px;line-height:1.85}
.wrap{width:980px;margin:0 auto;position:relative}
h2{font-weight:500;color:var(--ink);font-size:39px;line-height:1.35}
h2 span{color:var(--blue)}
.lead{font-weight:700;color:var(--ink);font-size:16px;margin-top:14px}
.btn{display:inline-block;background:var(--blue);color:#fff;font-weight:700;font-size:17px;padding:13px 19px;border-radius:5px;text-decoration:none}
.brand{font-family:'Lato',sans-serif;font-weight:400;font-size:28px;color:#555;letter-spacing:.3px;line-height:1}

/* header */
.topbar{height:83px;display:flex;align-items:center;padding:0 110px 0 72px;justify-content:space-between}
.topbar .contact{display:flex;gap:70px;font-size:14px;color:#333;align-items:center}
.topbar .contact span{display:flex;align-items:center;gap:10px}
.topbar .btn{padding:14px 26px;font-size:18px}
.nav{height:43px;background:var(--blue);display:flex;justify-content:center;align-items:center;gap:19px;font-size:14.5px;color:#fff}

/* hero */
.hero{height:474px;background:linear-gradient(90deg,#5d5f60,#9a9c9d 45%,#c9cbcc);text-align:center;color:#fff;padding-top:62px;position:relative}
.hero h1{font-size:51px;font-weight:700;line-height:1.17;text-shadow:0 2px 6px rgba(0,0,0,.5)}
.hero p{width:760px;margin:26px auto 0;font-size:14.5px;line-height:1.8;text-shadow:0 1px 3px rgba(0,0,0,.6)}
.hero .btn{margin-top:26px;padding:14px 30px}

/* about */
.about{height:519px;position:relative;overflow:hidden}
.about .copy{position:absolute;left:110px;top:72px;width:455px}
.about .copy p{margin-top:0}
.about .btn{margin-top:22px}
.blob{position:absolute;left:785px;top:233px;width:620px;height:620px;border-radius:50%;background:var(--sky-soft)}
.blob2{position:absolute;left:800px;top:250px;width:620px;height:620px;border-radius:50%;background:var(--sky)}
.frame{position:absolute;border:4px solid var(--sky);}
.photo{position:absolute}
.about .badge{position:absolute;left:855px;top:1030px}
.about .sig{position:absolute;left:870px;top:440px;color:#fff;font-size:36px;font-weight:400;border-top:1px solid rgba(255,255,255,.6);border-bottom:1px solid rgba(255,255,255,.6);padding:6px 10px}

/* approach */
.approach{height:513px;background:var(--tint);text-align:center;padding-top:72px}
.approach .lead{margin-top:16px}
.approach .sub{font-size:14.5px;width:980px;margin:2px auto 0}
.cols{display:flex;width:980px;margin:4px auto 0}
.col{flex:1;padding:24px 40px 0;height:222px}
.col+.col{border-left:1px solid #bbb}
.icon{width:108px;height:96px;border-radius:6px;background:var(--blue);margin:0 auto 14px}

/* planning */
.planning{height:570px;position:relative}
.planning .copy{position:absolute;left:640px;top:70px;width:450px}

/* pre */
.pre{height:543px;background:var(--tint);position:relative}
.pre .copy{position:absolute;left:110px;top:68px;width:450px}
.pre ul{list-style:none;margin-top:20px}
.pre li{display:flex;gap:14px;font-size:14.5px}
.pre li svg{flex:none;margin-top:6px}

/* post */
.post{height:609px;text-align:center;padding-top:72px}
.post .lead{margin-top:6px}
.post .sub{margin-top:14px}
.cards{display:flex;gap:24px;width:980px;margin:12px auto 0}
.card{flex:1;background:#fff;box-shadow:0 3px 10px rgba(0,0,0,.15);height:307px}
.card .img{height:210px}
.card p{font-size:17px;color:var(--ink);line-height:1.6;padding:11px 30px}
.card.active{background:var(--sky);border:2px solid var(--blue)}
.card.active p{color:#fff}

/* commitment */
.commit{height:409px;background:var(--tint);text-align:center;padding-top:65px}
.commit .lead{margin-top:16px}
.commit .sub{width:980px;margin:0 auto}
.commit .btn{margin-top:22px}

/* footer */
.footer{height:336px;background:var(--blue);color:#fff;position:relative}
.footer h4{font-size:21px;font-weight:700;margin-bottom:4px}
.footer .f1{position:absolute;left:110px;top:82px}
.footer .f2{position:absolute;left:480px;top:73px}
.footer .f3{position:absolute;left:800px;top:73px}
.footer ul{list-style:none;font-size:14.5px;line-height:1.98}
.footer ul li::before{content:"";display:inline-block;width:8px;height:8px;background:#fff;margin-right:12px;vertical-align:middle}
.footer .row{display:flex;gap:10px;font-size:14.5px;margin-top:8px;line-height:1.7}
.socials{display:flex;gap:14px;margin-top:48px}
.socials i{width:27px;height:27px;border-radius:50%;background:#fff;display:block}
.footer .copy{position:absolute;left:110px;right:110px;top:288px;border-top:1px solid rgba(255,255,255,.35);text-align:center;font-size:14.5px;padding-top:16px}
</style>
</head>
<body>

<header class="topbar">
  <div class="brand">Dr. Renato Vilhena</div>
  <div class="contact">
    <span><svg width="22" height="22" viewBox="0 0 24 24"><path fill="#1f4f9f" d="M6.6 10.8c1.4 2.8 3.8 5.1 6.6 6.6l2.2-2.2c.3-.3.7-.4 1-.2 1.1.4 2.3.6 3.6.6.6 0 1 .4 1 1V20c0 .6-.4 1-1 1A17 17 0 0 1 3 4c0-.6.4-1 1-1h3.5c.6 0 1 .4 1 1 0 1.3.2 2.5.6 3.6.1.3 0 .7-.2 1z"/></svg>888 888 88</span>
    <span><svg width="22" height="16" viewBox="0 0 22 16"><rect x="1" y="1" width="20" height="14" rx="1" fill="none" stroke="#1f4f9f" stroke-width="2"/><path d="M1 1l10 8 10-8" fill="none" stroke="#1f4f9f" stroke-width="2"/></svg>dr.renato@vilhenaclinica.com.br</span>
  </div>
  <a class="btn">Contato</a>
</header>
<nav class="nav">
  <span>Sobre o Dr. Renato Vilhena</span><span>Nossa Abordagem</span><span>Planejamento com Tecnologia 3D</span><span>Apoio Pré-Procedimento</span><span>Cuidado no Pós-Operatório</span>
</nav>

<section class="hero" role="img" aria-label="Fotografia de consultório médico moderno ao fundo">
  <h1>Cuidar Com Precisão,<br>Tratar Com Empatia</h1>
  <p>A cirurgia robótica representa um dos avanços mais relevantes da medicina moderna. Ela oferece mais precisão, menor sangramento e uma recuperação mais rápida. Mas, acima da tecnologia, está o compromisso com a melhor decisão para cada paciente.</p>
  <a class="btn">Comece</a>
</section>

<section class="about">
  <div class="copy">
    <h2>Sobre o <span>Dr. Renato Vilhena</span></h2>
    <p class="lead">Cuidar com precisão, tratar com empatia</p>
    <p>Sou urologista com foco em cirurgia robótica e atenção integral ao paciente. Mais do que uma técnica, acredito que a boa medicina começa pela escuta, pelo planejamento cuidadoso e pelo compromisso com o que há de melhor para cada pessoa. Minha missão é oferecer tratamentos baseados em ciência, tecnologia e humanidade — respeitando o tempo, as escolhas e os objetivos de cada paciente.</p>
    <a class="btn">Leia mais</a>
  </div>
  <div class="blob"></div>
  <div class="blob2"></div>
  <div class="frame" style="left:721px;top:84px;width:290px;height:340px;border-color:var(--sky)"></div>
  <div class="photo" role="img" aria-label="Retrato do médico de jaleco branco" style="left:727px;top:93px;width:284px;height:338px;background:linear-gradient(180deg,#9a6a3e,#d9d4cc 55%,#f1f1f1)"></div>
  <div class="sig">Dr. Renato Vilhena</div>
</section>

<section class="approach">
  <h2>Nossa <span>Abordagem</span></h2>
  <p class="lead">Nem todo tratamento precisa ser cirúrgico. Nem toda cirurgia precisa ser robótica.</p>
  <p class="sub">A cirurgia robótica é um grande avanço, mas deve ser indicada com critério. Antes de propor qualquer intervenção, avaliamos o caso de forma ampla</p>
  <div class="cols">
    <div class="col"><div class="icon" role="img" aria-label="Ícone de calendário médico"></div>Utilizamos os <b style="color:#333;font-weight:500">guidelines médicos mais atualizados</b></div>
    <div class="col"><div class="icon" role="img" aria-label="Ícone de inteligência artificial"></div>Fazemos uso de ferramentas de inteligência artificial para apoiar a decisão clínica</div>
    <div class="col"><div class="icon" role="img" aria-label="Ícone de balança de decisão"></div>Conduzimos conversas francas sobre as reais necessidades, benefícios e riscos de cada abordagem.</div>
  </div>
</section>

<section class="planning">
  <div class="frame" style="left:110px;top:108px;width:452px;height:336px;border-color:var(--blue)"></div>
  <div class="photo" role="img" aria-label="Modelo anatômico 3D de rins e vasos sanguíneos" style="left:120px;top:117px;width:448px;height:335px;background:linear-gradient(135deg,#8e94d8,#c9a98c 50%,#9aa0e0)"></div>
  <div class="copy">
    <h2>Planejamento <span>com Tecnologia 3D</span></h2>
    <p class="lead">Ver além da imagem: planejar com profundidade.</p>
    <p>Em cirurgias renais e prostáticas, adotamos o uso de modelos 3D personalizados, criados a partir dos exames do próprio paciente. Esses modelos ajudam a compreender a anatomia de forma precisa, facilitando a escolha da melhor abordagem cirúrgica.<br>Já demonstramos que esse planejamento reduz sangramentos, o tempo cirúrgico e até mesmo muda a estratégia em quase metade dos casos avaliados.</p>
    <a class="btn" style="margin-top:22px">Leia mais</a>
  </div>
</section>

<section class="pre">
  <div class="copy">
    <h2>Apoio <span>Pré-Procedimento</span></h2>
    <p class="lead">Seu foco deve ser sua saúde, não a burocracia.</p>
    <p style="margin-top:8px">Sabemos que o momento que antecede um procedimento pode ser cercado de dúvidas e ansiedade. Por isso, oferecemos:</p>
    <ul>
      <li><svg width="20" height="20" viewBox="0 0 20 20"><circle cx="10" cy="10" r="8.5" fill="none" stroke="#1f4f9f" stroke-width="1.5"/><path d="M5.5 10h8M10.5 6.5l3.5 3.5-3.5 3.5" fill="none" stroke="#1f4f9f" stroke-width="1.5"/></svg><span>Um escritório dedicado a resolver toda a parte burocrática com hospitais e convênios;</span></li>
      <li><svg width="20" height="20" viewBox="0 0 20 20"><circle cx="10" cy="10" r="8.5" fill="none" stroke="#1f4f9f" stroke-width="1.5"/><path d="M5.5 10h8M10.5 6.5l3.5 3.5-3.5 3.5" fill="none" stroke="#1f4f9f" stroke-width="1.5"/></svg><span>Suporte próximo, ágil e humano, para que você se concentre no que realmente importa: sua preparação e bem-estar.</span></li>
    </ul>
    <a class="btn" style="margin-top:22px">Leia mais</a>
  </div>
  <div class="frame" style="left:632px;top:84px;width:452px;height:352px;border-color:var(--blue)"></div>
  <div class="photo" role="img" aria-label="Médica conversando com uma criança" style="left:642px;top:94px;width:447px;height:346px;background:linear-gradient(120deg,#1d4a5a,#2e7488 50%,#0f2f3c)"></div>
</section>

<section class="post">
  <h2>Cuidado no <span>Pós-Operatório</span></h2>
  <p class="lead">Recuperar bem é parte essencial do tratamento.</p>
  <p class="sub">Após a alta hospitalar, continuamos ao seu lado. Nosso time de enfermeiras e fisioterapeutas oferece</p>
  <div class="cards">
    <div class="card"><div class="img" role="img" aria-label="Médica em visita domiciliar a paciente" style="background:linear-gradient(135deg,#d8d6d2,#f2f1ee)"></div><p>Visitas domiciliares quando necessário</p></div>
    <div class="card active"><div class="img" role="img" aria-label="Profissional orientando paciente em consulta" style="background:linear-gradient(135deg,#6a7a8c,#d9d3c8)"></div><p>Orientações práticas sobre movimentação, alimentação e medicações</p></div>
    <div class="card"><div class="img" role="img" aria-label="Médico examinando uma menina sorridente" style="background:linear-gradient(135deg,#2a3a48,#c79a7e)"></div><p>Monitoramento de sinais que mereçam atenção — sempre com o olhar clínico atento.</p></div>
  </div>
</section>

<section class="commit">
  <h2>Compromisso <span>com o Paciente</span></h2>
  <p class="lead">Acreditamos que o melhor resultado vem da soma entre conhecimento, tecnologia e empatia.</p>
  <p class="sub">Nosso compromisso é entender profundamente o que você está enfrentando, apresentar com clareza todas as opções disponíveis e construir, juntos, o melhor caminho para o seu tratamento.<br>Porque cada paciente é único — e merece ser cuidado como tal.</p>
  <a class="btn">Leia mais</a>
</section>

<footer class="footer">
  <div class="f1">
    <div class="brand" style="color:#fff">Dr. Renato Vilhena</div>
    <div class="socials"><i></i><i></i><i></i><i></i></div>
  </div>
  <div class="f2">
    <h4>Quick Links</h4>
    <ul><li>Sobre o Dr. Renato Vilhena</li><li>Nossa Abordagem</li><li>Planejamento com Tecnologia 3D</li><li>Apoio Pré-Procedimento</li><li>Cuidado no Pós-Operatório</li></ul>
  </div>
  <div class="f3">
    <h4>Contact Us</h4>
    <div class="row"><svg width="26" height="26" viewBox="0 0 26 26"><circle cx="13" cy="13" r="13" fill="#fff"/><path fill="#1f4f9f" d="M9.5 11.5c.9 1.8 2.4 3.2 4.1 4.1l1.4-1.4c.2-.2.4-.2.6-.1.7.2 1.4.4 2.2.4.4 0 .6.3.6.6v2.2c0 .4-.2.6-.6.6A10.4 10.4 0 0 1 7.2 7.6c0-.4.3-.6.6-.6H10c.4 0 .6.2.6.6 0 .8.1 1.5.4 2.2 0 .2 0 .4-.2.6z"/></svg>888 888 88</div>
    <div class="row"><svg width="26" height="26" viewBox="0 0 26 26"><circle cx="13" cy="13" r="13" fill="#fff"/><rect x="7" y="9" width="12" height="8" fill="none" stroke="#1f4f9f" stroke-width="1.5"/><path d="M7 9l6 5 6-5" fill="none" stroke="#1f4f9f" stroke-width="1.5"/></svg>dr.renato@vilhenaclinica.com.br</div>
    <div class="row"><svg width="26" height="26" viewBox="0 0 26 26"><circle cx="13" cy="13" r="13" fill="#fff"/><path fill="#1f4f9f" d="M13 6a5 5 0 0 0-5 5c0 3.8 5 9 5 9s5-5.2 5-9a5 5 0 0 0-5-5zm0 7a2 2 0 1 1 0-4 2 2 0 0 1 0 4z"/></svg><span>Av. Exemplo da Saúde, 123 – Sala 456<br>São Paulo – SP | CEP 00000-000</span></div>
  </div>
  <div class="copy">Copyright ©2025 Dr. Renato Vilhena. Todos os direitos reservados.</div>
</footer>

</body>
</html>
```